Redesign Application Page for Job Position

Would like to get a redesign on our Job Application Page.
You can use brennoxguard or valmoreta as references.

http://www.careersatklv.example/KLV/NCreateAccount.aspx?aga=qwtrzx4hemLK7

Target Market(s)

Professional Security Individuals

Industry/Entity Type

Security Guard

Coding

Coded - Design and coding required

Number of Pages Required

1 page

Font styles to use
Sans Serif

Colors
0255a3
3276b5
ffcf3e
fee18a

Requirements
Must have
• User Friendly, Easy Navigation. Must be very easy to read and understand what is required or missing.
Should not have
• Ugly or Bulky

```html
<!DOCTYPE html>
<html lang="en">
<head>
<meta charset="utf-8">
<title>Create an Application – Keller Valley Guard Services</title>
<link href="https://fonts.googleapis.com/css2?family=Open+Sans:wght@400;600;700&display=swap" rel="stylesheet">
<style>
:root{
  --brand:#0255a3;
  --brand-mid:#3276b5;
  --banner:#2f62a6;
  --navy:#0a3a86;
  --footer:#0b3c8c;
  --gold:#ffcf3e;
  --gold-deep:#f7bb1c;
  --gold-soft:#fee18a;
  --ink:#2b2b2b;
  --muted:#5a5a5a;
  --field-border:#c9c9c9;
  --placeholder:#8a8a8a;
  --row:#f3f3f3;
  --line:#d8d8d8;
}
*{box-sizing:border-box;margin:0;padding:0}
html,body{width:1200px;height:2169px;overflow:hidden}
body{position:relative;background:#fff;font-family:"Open Sans",Arial,sans-serif;color:var(--ink)}

.site-header{position:absolute;left:0;top:0;width:1200px;height:90px;background:#fff}
.brand{position:absolute;left:152px;top:18px;display:flex;align-items:center;gap:16px}
.brand-dot{width:60px;height:60px;border-radius:50%;background:var(--brand)}
.brand-name{font-weight:700;font-size:23px;line-height:23px;color:var(--brand);text-transform:uppercase}

.hero{position:absolute;left:0;top:90px;width:1200px;height:395px;
  background:linear-gradient(100deg,#d9d4cc 0%,#e9e6e1 30%,#cfc9c0 50%,#8d8b88 62%,#5e7392 75%,#6e7f97 88%,#4c4a48 100%)}
.hero-banner{position:absolute;left:0;top:182px;width:536px;height:90px;background:var(--banner);
  display:flex;align-items:center;padding-left:137px;color:#fff;font-size:28px;font-weight:400;letter-spacing:.5px}

.intro{position:absolute;left:126px;top:532px;width:910px;font-size:14.6px;line-height:24.5px;color:var(--muted)}
.instructions{position:absolute;left:126px;top:634px;font-size:20px;color:var(--ink)}

.application-card{position:absolute;left:126px;top:706px;width:820px;height:1340px;background:#fff;
  box-shadow:0 0 6px rgba(0,0,0,.25)}
.application-card > *{position:absolute}
.date-created{left:36px;top:40px;font-size:16px;color:var(--ink)}

.field{height:41px;border:1px solid var(--field-border);background:#fff;font-size:15px;color:var(--placeholder);
  display:flex;align-items:center;justify-content:space-between;padding:0 14px}
.field svg{width:16px;height:10px}
.section-label{font-size:16.5px;color:var(--brand)}
.option{display:inline-flex;align-items:center;gap:8px;font-size:15px;color:var(--muted)}
.radio{width:17px;height:17px;border-radius:50%;border:1px solid #b5b5b5;background:#fafafa;display:inline-block}
.checkbox{width:15px;height:15px;border:1px solid #b5b5b5;background:#fafafa;display:inline-block}

.license-heading{left:42px;top:451px;font-size:20px;font-weight:600;color:var(--brand)}
.data-table{border-collapse:collapse;width:743px}
.data-table th{background:linear-gradient(var(--gold),var(--gold-deep));color:#333;font-weight:600;font-size:14.5px;text-align:left;height:35px;padding:0 20px}
.license-table td{height:41px;border-top:1px solid #fff;border-bottom:1px solid var(--line);background:var(--row);font-size:14px;color:#333;padding:0 20px}
.license-table td + td{border-left:1px solid var(--line);padding:0 10px}
.license-table td.small{font-size:11px}
.cell-input{height:29px;border:1px solid var(--field-border);background:#fff;display:flex;align-items:center;gap:10px;padding:0 10px;font-size:13px;color:var(--placeholder)}

.availability-table th{text-align:center;height:40px;font-size:16px;padding:0}
.availability-table td{height:37px;border-bottom:1px solid var(--line);text-align:center;font-size:15px;color:var(--brand);vertical-align:middle}
.availability-table td:first-child{border-right:1px solid var(--line)}
.availability-table tr:last-child td{height:47px;border-bottom:1px solid var(--line)}
.availability-table .radio{vertical-align:middle}

.btn{width:208px;height:46px;display:flex;align-items:center;justify-content:center;font-size:20px;color:#fff}
.btn-continue{background:linear-gradient(var(--brand),var(--navy))}
.btn-discard{background:linear-gradient(var(--gold),var(--gold-deep))}
.help{font-size:14.5px;color:var(--ink)}
.help strong{font-weight:600}

.site-footer{position:absolute;left:0;top:2102px;width:1200px;height:67px;background:var(--footer);
  display:flex;align-items:center;justify-content:center;font-size:14px;color:#b9c9e4}
</style>
</head>
<body>

<header class="site-header">
  <div class="brand">
    <span class="brand-dot"></span>
    <div class="brand-name">Keller Valley Guard<br>Services, Inc.</div>
  </div>
</header>

<section class="hero" role="img" aria-label="Photo of a man in glasses working on a laptop in a bright room">
  <h1 class="hero-banner">CREATE AN APPLICATION</h1>
</section>

<p class="intro">Vivamus porttitor purus nisi eleifend libero a tempus libero lectus feugiat felis Morbi diam mauris viverra in gravida eu mattis in ante Morbi eget arcu Morbi porta libero id ullamcorper nonummy nibh ligula pulvinar metus eget consectetuer augue nisi quis lacus eros Curabitur vel mi sit amet magna malesuada ultrices Ut nisi erat fermentum vel congue id euismod in elit Fusce ultricies orci ac feugiat</p>
<p class="instructions">Complete all required fields , then click "Continue" to create your account!</p>

<svg width="0" height="0" style="position:absolute">
  <defs>
    <symbol id="chevron" viewBox="0 0 16 10"><path d="M1 1l7 7 7-7" fill="none" stroke="#444" stroke-width="2"/></symbol>
    <symbol id="calendar" viewBox="0 0 16 16"><rect x="1" y="3" width="14" height="12" fill="none" stroke="#999"/><rect x="1" y="3" width="14" height="3" fill="#999"/><path d="M4 9h2M7 9h2M10 9h2M4 12h2M7 12h2M10 12h2" stroke="#999"/><path d="M4 1v3M12 1v3" stroke="#999"/></symbol>
  </defs>
</svg>

<main class="application-card">
  <p class="date-created">Date Created: 04-Jan-2018</p>

  <div class="field" style="left:36px;top:79px;width:241px">First Name*</div>
  <div class="field" style="left:287px;top:79px;width:241px">Middle Name</div>
  <div class="field" style="left:538px;top:79px;width:241px">Last Name*</div>

  <p class="section-label" style="left:36px;top:131px">Gender</p>
  <div style="left:40px;top:168px;display:flex;gap:46px">
    <span class="option"><span class="radio"></span>Male</span>
    <span class="option"><span class="radio"></span>Female</span>
  </div>
  <p class="section-label" style="left:289px;top:131px">Date of Birth</p>
  <div class="field" style="left:289px;top:163px;width:157px">Month<svg><use href="#chevron"/></svg></div>
  <div class="field" style="left:455px;top:163px;width:157px">Day<svg><use href="#chevron"/></svg></div>
  <div class="field" style="left:621px;top:163px;width:158px">Year<svg><use href="#chevron"/></svg></div>

  <div class="field" style="left:37px;top:224px;width:239px">Street Address*</div>
  <div class="field" style="left:289px;top:224px;width:239px">Select City</div>
  <div class="field" style="left:538px;top:224px;width:241px">Select State<svg><use href="#chevron"/></svg></div>

  <div class="field" style="left:40px;top:279px;width:237px">Nearest Office<svg><use href="#chevron"/></svg></div>
  <div class="field" style="left:290px;top:279px;width:239px">Zip*</div>

  <div class="field" style="left:40px;top:334px;width:237px">Cell Number</div>
  <div class="field" style="left:290px;top:334px;width:239px">Home Phone Number</div>

  <div class="field" style="left:40px;top:389px;width:237px">Select Job Position<svg><use href="#chevron"/></svg></div>
  <div class="field" style="left:290px;top:389px;width:239px">SSN*</div>

  <h2 class="license-heading">License Details</h2>
  <table class="data-table license-table" style="left:42px;top:491px">
    <thead><tr><th style="width:406px">TYPE</th><th style="width:163px;padding-left:14px">NUMBER</th><th style="padding-left:18px">EXPIRE DATE</th></tr></thead>
    <tbody>
      <tr><td>Guard Card</td><td><div class="cell-input"></div></td><td><div class="cell-input"><svg width="16" height="16"><use href="#calendar"/></svg>MM/DD/YY</div></td></tr>
      <tr><td>Baton</td><td><div class="cell-input"></div></td><td><div class="cell-input"><svg width="16" height="16"><use href="#calendar"/></svg>MM/DD/YY</div></td></tr>
      <tr><td>Gun Permit</td><td><div class="cell-input"></div></td><td><div class="cell-input"><svg width="16" height="16"><use href="#calendar"/></svg>MM/DD/YY</div></td></tr>
      <tr><td>Transportation Workers Identification Card (TWIC)</td><td><div class="cell-input"></div></td><td><div class="cell-input"><svg width="16" height="16"><use href="#calendar"/></svg>MM/DD/YY</div></td></tr>
      <tr><td>Merchant Mariner Credential (MMC)</td><td><div class="cell-input"></div></td><td><div class="cell-input"><svg width="16" height="16"><use href="#calendar"/></svg>MM/DD/YY</div></td></tr>
      <tr><td class="small">Standards of Training, Certification and Watchkeeping for Seafarers (SCTW)</td><td><div class="cell-input"></div></td><td><div class="cell-input"><svg width="16" height="16"><use href="#calendar"/></svg>MM/DD/YY</div></td></tr>
    </tbody>
  </table>

  <p class="section-label" style="left:46px;top:794px">ID Document Type :</p>
  <div class="field" style="left:48px;top:830px;width:232px">Select<svg><use href="#chevron"/></svg></div>

  <p class="section-label" style="left:309px;top:798px">Additional Languages :</p>
  <div style="left:309px;top:830px;display:flex;gap:18px">
    <span class="option"><span class="checkbox"></span>Spanish</span>
    <span class="option"><span class="checkbox"></span>French</span>
    <span class="option"><span class="checkbox"></span>Japanese</span>
    <span class="option"><span class="checkbox"></span>Chinese</span>
  </div>

  <div class="field" style="left:48px;top:896px;width:232px">Email address*</div>
  <p class="section-label" style="left:314px;top:901px">How did you hear about us?</p>
  <div class="field" style="left:545px;top:890px;width:234px">Select<svg><use href="#chevron"/></svg></div>

  <p class="section-label" style="left:46px;top:961px">Work Availability :</p>
  <table class="data-table availability-table" style="left:42px;top:1003px">
    <thead><tr><th style="width:115px">Shift</th><th>Sun</th><th>Mon</th><th>Tue</th><th>Wed</th><th>Thu</th><th>Fri</th><th>Sat</th></tr></thead>
    <tbody>
      <tr><td>Day Shift</td><td><span class="radio"></span></td><td><span class="radio"></span></td><td><span class="radio"></span></td><td><span class="radio"></span></td><td><span class="radio"></span></td><td><span class="radio"></span></td><td><span class="radio"></span></td></tr>
      <tr><td>Swing Shift</td><td><span class="radio"></span></td><td><span class="radio"></span></td><td><span class="radio"></span></td><td><span class="radio"></span></td><td><span class="radio"></span></td><td><span class="radio"></span></td><td><span class="radio"></span></td></tr>
      <tr><td>Night Shift</td><td><span class="radio"></span></td><td><span class="radio"></span></td><td><span class="radio"></span></td><td><span class="radio"></span></td><td><span class="radio"></span></td><td><span class="radio"></span></td><td><span class="radio"></span></td></tr>
    </tbody>
  </table>

  <div class="btn btn-continue" style="left:43px;top:1200px">Continue</div>
  <div class="btn btn-discard" style="left:266px;top:1200px">Discard</div>

  <p class="help" style="left:46px;top:1266px">Need Help? Call us at: <strong>(310)555-0142</strong> and ask for a Human Resource representative.</p>
</main>

<footer class="site-footer">© 2018 Company Name &nbsp;All right reserved &nbsp;Terms of Use</footer>

</body>
</html>
```